依頼詳細
【デザインテイストについて】
カジュアル・ゴージャス・にぎやか・ナチュラル・優しい・パステル
シンプル・清潔な・重厚感

【デザインカラーについて】
サロンの内装にレンガがあるのですが、私が直接施工してまして
それはもし可能であれば、サイトのデザイン内に組み込んで頂ければ
とても嬉しいです。

【参考にしているデザイン】
インテリア本:Hearth Leaf Digest
本内のデザインや見せ方が好みです。
https://hearthleaf.jp/cp/hearthleafdigest

【その他】
●「http://morvelin-salon.com/」のページ下部にあるlinkora部分の様に
サイトの中に挿入したいと考えています。
見本で構いませんので、画像で貼り付けて頂ければ嬉しいです。

●ルナリボンに飛ばす物も良ければ配置してほしいです。

【ページ項目】
①トップページ
②サロン紹介
③スタッフ紹介
④お知らせ
⑤ブログ
⑥スタイルギャラリー
⑦コンセプト
⑧商品紹介
⑨よくある質問
⑩メニュー
⑪クーポン
⑫フリーマーケット
⑬レビュー投稿(お問い合わせのフォーム)
⑭お客様の声

サイトURL
http://beauty.lunaribbon.jp/slnK000584127/
ページ数
1ページ
希望イメージ
シンプル 複雑
単色 カラフル
暗い 明るい
日常 高級
遊び心 厳粛
未来的 伝統的
女性的 男性的
希望する色
ベージュ、グリーン、茶色
納品ファイル
• 高解像度JPG (.jpg)
• イラストレーター形式 (.ai)
• フォトショップ形式 (.psd)
• PNG形式 (.png)
補足説明
----------------------------------------------------

【素材について】
※ロゴ
サロンのキャラクターがあるので、サイトの中で使って頂ければ幸いです。
http://filevaultbox.jp/download/9a3e7c10bd4f2a6695e0c7d81f4b2e07a6c9d315
ダウンロードパスワード:qzt4mu8r

※サロン写真
http://filevaultbox.jp/download/2c8b5f1e9d7a3064b1e2f8c5a9d0e7b3c4f6a821
ダウンロードパスワード:wld3pvoe

※その他
イメジオ「https://jp.imegio.com/」の定期契約内の画像は使用可能です。
イメジオ以外は無料の素材をご使用くださいませ。

ゴールデンウィーク中で大変申し訳ありませんが、一週間延長させて頂きます。
是非宜しくお願い致します。
■ 選んだ理由

一目ぼれしました!
とても目を引くデザインで、当サロンのイラストをうまく取り込んで頂いていルなと思い、選ばせて頂きました!

■ 提案者全員のお礼・コメント

沢山のご提案をして頂き、本当にありがとうございました!
とても嬉しく全てのデザインを使用したいところですが、コンペ形式にて1つしか選べないと言うのあとても心苦しく思っています。

またこのような機会がありましたら、ご協力頂けますと幸いです。
ありがとうございました。

```html
<!DOCTYPE html>
<html lang="ja">
<head>
<meta charset="utf-8">
<title>Mirelle</title>
<link rel="stylesheet" href="https://fonts.googleapis.com/css2?family=Oswald:wght@300;400&family=Noto+Sans+JP:wght@300;400&display=swap">
<style>
:root{
  --red:#e05a47;
  --green:#6e8a63;
  --ink:#444;
  --grey:#888;
  --line:#cfcfcf;
  --paper:#ffffff;
  --brick:#b3aba3;
}
*{margin:0;padding:0;box-sizing:border-box}
html,body{width:1200px;height:2648px;overflow:hidden;background:var(--paper)}
body{position:relative;font-family:"Oswald",sans-serif;font-weight:300;color:var(--ink)}
.abs{position:absolute}
.hero{left:0;top:0;width:1200px;height:540px;background:linear-gradient(120deg,#cfc8bd 0%,#e8e4dc 40%,#9ea196 75%,#6f7d69 100%)}
.brand{left:300px;top:160px;display:flex;align-items:center;gap:26px;color:var(--red);font-family:"Oswald",sans-serif;font-weight:400;font-size:120px;line-height:1}
.brand-mark{width:70px;height:70px;border-radius:50%;background:var(--red);flex:none}
.rule{height:4px;background:var(--red);left:100px;width:1000px}
.rule.thin{height:2px}
.nav{left:100px;top:604px;width:1000px;display:flex;justify-content:space-around;font-size:30px;color:var(--ink)}
.concept-title{left:196px;top:820px;font-size:32px;font-weight:300}
.concept-text{left:400px;top:796px;font-family:"Noto Sans JP",sans-serif;font-size:14px;line-height:30px;color:var(--grey);width:380px}
.concept-art{left:820px;top:730px;width:240px;height:250px;background:linear-gradient(180deg,#f2b8ac 0%,#e8d9c4 55%,#b7c9a7 100%);border-radius:8px}
.gallery{left:100px;top:1100px;width:1000px;height:250px;background:linear-gradient(90deg,#c6beb6,#a9a099);overflow:hidden}
.gallery svg{position:absolute;left:0;top:0}
.gallery-btn{left:400px;top:1200px;width:350px;height:76px;border:2px solid #fff;color:#fff;font-size:32px;display:flex;align-items:center;justify-content:center}
.tile{width:300px;height:210px}
.label{font-size:30px;color:var(--ink)}
.t-menu{left:100px;top:1460px;background:linear-gradient(135deg,#333,#5b5b58)}
.t-item{left:445px;top:1460px;background:linear-gradient(135deg,#d7d2c8,#8e8a80)}
.t-coupon{left:100px;top:1745px;background:linear-gradient(135deg,#3e3e3e,#a59f95)}
.t-market{left:445px;top:1745px;background:linear-gradient(135deg,#ece9e3,#b2aca2)}
.t-review{left:100px;top:2040px;background:linear-gradient(135deg,#f0ede7,#7e8a6a)}
.t-shop{left:445px;top:2040px;background:linear-gradient(135deg,#e6e2dc,#6c6a66)}
.side{left:800px;width:300px}
.side-head{font-size:34px;text-align:center;width:300px;font-weight:300}
.news-list{left:820px;top:1600px;font-family:"Noto Sans JP",sans-serif;font-size:14px;color:var(--grey);line-height:30px}
.news-list span{display:inline-block;width:90px}
.more{left:880px;top:1765px;width:160px;height:36px;border:1px solid var(--grey);font-size:16px;display:flex;align-items:center;justify-content:center;color:var(--grey)}
.widget{left:800px;top:2040px;width:300px;height:250px;background:linear-gradient(180deg,#f4f4f4,#dcdfe6);border:1px solid var(--line)}
.footer{left:0;top:2428px;width:1200px;height:220px;background:var(--red)}
.f-brand{left:100px;top:2452px;color:#fff;font-family:"Oswald",sans-serif;font-weight:400;font-size:30px;line-height:1}
.f-info{left:230px;top:2462px;color:#fff;font-family:"Noto Sans JP",sans-serif;font-size:12px;line-height:22px}
.f-hours{left:440px;top:2462px;color:#fff;font-family:"Noto Sans JP",sans-serif;font-size:12px;line-height:22px}
.f-tel{left:560px;top:2506px;color:#fff;font-family:"Noto Sans JP",sans-serif;font-size:12px}
.f-map{left:700px;top:2440px;width:400px;height:110px;background:linear-gradient(135deg,#f1efe9,#d7dbd0)}
.f-nav{left:100px;top:2586px;width:1000px;display:flex;justify-content:space-between;color:#fff;font-size:26px}
.f-nav span{border-bottom:2px solid #fff;padding:0 14px}
</style>
</head>
<body>
<div class="abs hero" role="img" aria-label="Photograph of the salon storefront with flowers by the door"></div>
<div class="abs brand"><span class="brand-mark"></span><span>Mirelle</span></div>

<div class="abs rule" style="top:584px"></div>
<div class="abs rule thin" style="top:594px"></div>
<nav class="abs nav"><span>Salon</span><span>Staff</span><span>Q and A</span><span>Blog</span></nav>
<div class="abs rule thin" style="top:660px"></div>
<div class="abs rule" style="top:666px"></div>

<h2 class="abs concept-title">Concept</h2>
<p class="abs concept-text">ここにテキストが入ります。ここにテキストが入ります。<br>ここにテキストが入ります。ここにテキストが入ります。<br>ここにテキストが入ります。ここにテキストが入ります。<br>ここにテキストが入ります。ここにテキストが入ります。</p>
<div class="abs concept-art" role="img" aria-label="Illustration of a customer relaxing under a hair dryer at a table"></div>
<div class="abs rule" style="top:1000px"></div>

<div class="abs gallery" role="img" aria-label="Photograph of the salon's hand-laid brick wall with a green band">
  <svg width="1000" height="250" viewBox="0 0 1000 250"><polygon points="270,0 1000,0 760,250 0,250" fill="var(--green)"/></svg>
</div>
<div class="abs gallery-btn">View the Gallery</div>
<div class="abs rule" style="top:1352px"></div>

<div class="abs tile t-menu" role="img" aria-label="Photograph of the salon menu chalkboard"></div>
<div class="abs label" style="left:100px;top:1672px">Menu</div>
<div class="abs tile t-item" role="img" aria-label="Photograph of hair care products on a shelf"></div>
<div class="abs label" style="left:445px;top:1672px">Item</div>
<div class="abs tile t-coupon" role="img" aria-label="Photograph of the salon entrance with an open sign"></div>
<div class="abs label" style="left:100px;top:1958px">Coupon</div>
<div class="abs tile t-market" role="img" aria-label="Photograph of framed pictures on a white wall"></div>
<div class="abs label" style="left:445px;top:1958px">Free market</div>
<div class="abs tile t-review" role="img" aria-label="Photograph of a potted plant"></div>
<div class="abs label" style="left:100px;top:2254px">Review</div>
<div class="abs tile t-shop" role="img" aria-label="Photograph of decorative tins on a counter"></div>
<div class="abs label" style="left:445px;top:2254px">Luna Ribbon</div>

<div class="abs rule side" style="top:1460px"></div>
<div class="abs rule thin side" style="top:1470px"></div>
<h3 class="abs side side-head" style="top:1510px">News</h3>
<div class="abs news-list">
  <div><span>2016/4/27</span>ここにテキストが入ります</div>
  <div><span>2016/4/27</span>ここにテキストが入ります</div>
  <div><span>2016/4/27</span>ここにテキストが入ります</div>
  <div><span>2016/4/27</span>ここにテキストが入ります</div>
</div>
<div class="abs more">More</div>
<div class="abs rule side" style="top:1860px"></div>
<div class="abs rule thin side" style="top:1870px"></div>
<h3 class="abs side side-head" style="top:1905px">Linkora</h3>
<div class="abs widget" role="img" aria-label="Embedded Linkora page feed for the salon"></div>

<div class="abs rule thin" style="top:2380px"></div>

<footer class="abs footer"></footer>
<div class="abs f-brand">Mirelle</div>
<div class="abs f-info">東京都港区架空町1-2-3<br>ミレルビル1F</div>
<div class="abs f-hours">Open 10:00-19:00<br>Closed on Wednesday</div>
<div class="abs f-tel">Tel 03-0000-0000</div>
<div class="abs f-map" role="img" aria-label="Street map showing the salon location"></div>
<nav class="abs f-nav"><span>TOP</span><span>voice</span><span>Blog</span><span>Review</span><span>Coupon</span><span>Luna Ribbon</span><span>Linkora</span></nav>
</body>
</html>
```